CFO services graphic design

I own a business consulting firm called Marlowe Consulting and we need a graphic for CFO services in our colours and branding. The attached file "CFO services to be put into Marlowe consulting theme", shows the content for the design. The two other files show the theme and colours for the new design.

```html
<!DOCTYPE html>
<html lang="en">
<head>
<meta charset="utf-8">
<title>Chief Financial Officer Services</title>
<link rel="stylesheet" href="https://fonts.googleapis.com/css2?family=Archivo+Black&family=Roboto:wght@400;700&display=swap">
<style>
  :root {
    --frame: #353333;
    --panel: #dcdcdc;
    --orange: #f2912f;
    --sky: #22a9e3;
    --royal: #1650bb;
    --navy: #08204b;
    --white: #ffffff;
  }
  html, body { margin: 0; padding: 0; overflow: hidden; }
  body { width: 1200px; height: 1200px; background: var(--frame); }
  .canvas { display: block; width: 1200px; height: 1200px; }
  .segment-title { font-family: "Roboto", Arial, sans-serif; font-weight: 700; font-size: 21px; fill: var(--white); text-anchor: middle; dominant-baseline: middle; }
  .segment-detail { font-family: "Roboto", Arial, sans-serif; font-weight: 400; font-size: 17px; fill: var(--white); text-anchor: middle; dominant-baseline: middle; }
  .hub-title { font-family: "Archivo Black", "Arial Black", sans-serif; font-size: 41px; fill: var(--navy); text-anchor: middle; dominant-baseline: middle; }
  .icon-badge { stroke: var(--white); stroke-width: 5; }
  .glyph { fill: none; stroke: var(--white); stroke-width: 4; stroke-linecap: round; stroke-linejoin: round; }
  .glyph-fill { fill: var(--white); }
</style>
</head>
<body>
<svg class="canvas" viewBox="0 0 1200 1200" xmlns="http://www.w3.org/2000/svg">
  <rect class="panel" x="81" y="81" width="1038" height="1038" fill="var(--panel)"/>

  <!-- wheel segments, clockwise from top -->
  <g class="wheel">
    <path fill="var(--orange)" d="M600 600 L446.5 229.5 A401 401 0 0 1 753.5 229.5 Z"/>
    <path fill="var(--sky)"    d="M600 600 L753.5 229.5 A401 401 0 0 1 970.5 446.5 Z"/>
    <path fill="var(--royal)"  d="M600 600 L970.5 446.5 A401 401 0 0 1 970.5 753.5 Z"/>
    <path fill="var(--navy)"   d="M600 600 L970.5 753.5 A401 401 0 0 1 753.5 970.5 Z"/>
    <path fill="var(--orange)" d="M600 600 L753.5 970.5 A401 401 0 0 1 446.5 970.5 Z"/>
    <path fill="var(--sky)"    d="M600 600 L446.5 970.5 A401 401 0 0 1 229.5 753.5 Z"/>
    <path fill="var(--royal)"  d="M600 600 L229.5 753.5 A401 401 0 0 1 229.5 446.5 Z"/>
    <path fill="var(--navy)"   d="M600 600 L229.5 446.5 A401 401 0 0 1 446.5 229.5 Z"/>
  </g>

  <!-- gaps between segments -->
  <g class="wheel-gaps" stroke="var(--panel)" stroke-width="18">
    <line x1="430" y1="190" x2="770" y2="1010"/>
    <line x1="770" y1="190" x2="430" y2="1010"/>
    <line x1="190" y1="430" x2="1010" y2="770"/>
    <line x1="190" y1="770" x2="1010" y2="430"/>
  </g>

  <circle class="hub-ring" cx="600" cy="600" r="177" fill="var(--white)" fill-opacity="0.3"/>
  <circle class="hub" cx="600" cy="600" r="151" fill="var(--white)"/>
  <text class="hub-title" x="602" y="564">Chief</text>
  <text class="hub-title" x="602" y="607">Financial</text>
  <text class="hub-title" x="602" y="650">Officer</text>

  <!-- segment labels -->
  <text class="segment-title" x="599" y="282">Cost Accounting</text>
  <text class="segment-title" x="599" y="308">&amp; Cost</text>
  <text class="segment-title" x="599" y="334">Management</text>

  <text class="segment-title" x="809" y="392">Capital Structure</text>
  <text class="segment-title" x="809" y="418">&amp; the</text>
  <text class="segment-title" x="809" y="444">Cost of Capital</text>

  <text class="segment-title" x="870" y="571">Long-term &amp;</text>
  <text class="segment-title" x="870" y="597">Short-term</text>
  <text class="segment-title" x="870" y="623">Investment</text>
  <text class="segment-title" x="870" y="649">Decisions</text>

  <text class="segment-title" x="822" y="793">Performance</text>
  <text class="segment-title" x="822" y="819">Evaluation</text>

  <text class="segment-title" x="599" y="873">Budgeting</text>
  <text class="segment-title" x="599" y="899">&amp; Strategic</text>
  <text class="segment-title" x="599" y="925">Planning</text>

  <text class="segment-title" x="390" y="793">Risk</text>
  <text class="segment-title" x="390" y="819">Management</text>

  <text class="segment-title" x="329" y="583">Compliance:</text>
  <text class="segment-detail" x="329" y="612">Tax, Legal and</text>
  <text class="segment-detail" x="329" y="631">Regulatory</text>

  <text class="segment-title" x="383" y="393">Communication:</text>
  <text class="segment-detail" x="383" y="419">Board of Directors,</text>
  <text class="segment-detail" x="383" y="438">creditors, owners, investors,</text>
  <text class="segment-detail" x="383" y="457">credit rating agencies</text>

  <!-- icon badges -->
  <g class="icon-cost" transform="translate(600 195)">
    <circle class="icon-badge" r="54" fill="var(--orange)"/>
    <rect class="glyph" x="-26" y="-32" width="34" height="50" rx="3"/>
    <circle class="glyph" cx="-9" cy="-17" r="9" stroke-width="3"/>
    <path class="glyph" d="M-21 2 l3 3 l5 -6 M-21 12 l3 3 l5 -6" stroke-width="3"/>
    <rect class="glyph-fill" x="0" y="-2" width="28" height="36" rx="3"/>
    <rect x="5" y="3" width="18" height="7" fill="var(--orange)"/>
    <path d="M5 15 h5 v5 h-5z M12 15 h5 v5 h-5z M19 15 h4 v5 h-4z M5 23 h5 v5 h-5z M12 23 h5 v5 h-5z M19 23 h4 v5 h-4z" fill="var(--orange)"/>
  </g>

  <g class="icon-capital" transform="translate(886 316)">
    <circle class="icon-badge" r="54" fill="var(--sky)"/>
    <path class="glyph-fill" d="M-10 -28 h20 l-5 8 a22 22 0 1 1 -10 0 z"/>
    <text x="0" y="3" font-family="Roboto, sans-serif" font-weight="700" font-size="20" fill="var(--sky)" text-anchor="middle" dominant-baseline="middle">$</text>
    <path class="glyph" d="M-32 18 l14 -6 h16 l22 -8 M-36 14 l8 20"/>
  </g>

  <g class="icon-investment" transform="translate(1005 600)">
    <circle class="icon-badge" r="54" fill="var(--royal)"/>
    <path class="glyph-fill" d="M-22 -32 h20 l-5 9 a24 24 0 1 1 -10 0 z"/>
    <text x="-12" y="6" font-family="Roboto, sans-serif" font-size="24" fill="var(--royal)" text-anchor="middle" dominant-baseline="middle">$</text>
    <circle cx="16" cy="20" r="16" fill="var(--royal)" stroke="var(--white)" stroke-width="4"/>
    <path class="glyph" d="M16 10 v10 l-6 5" stroke-width="3"/>
  </g>

  <g class="icon-performance" transform="translate(886 893)">
    <circle class="icon-badge" r="54" fill="var(--navy)"/>
    <path class="glyph-fill" d="M0 -40 l3 7 h7 l-6 4 2 7 -6 -4 -6 4 2 -7 -6 -4 h7z"/>
    <path class="glyph-fill" d="M-23 -30 l2 6 h6 l-5 3 2 6 -5 -4 -5 4 2 -6 -5 -3 h6z"/>
    <path class="glyph-fill" d="M23 -30 l2 6 h6 l-5 3 2 6 -5 -4 -5 4 2 -6 -5 -3 h6z"/>
    <path class="glyph" d="M-32 28 a32 32 0 0 1 64 0" stroke-width="10" stroke-linecap="butt"/>
    <path class="glyph" d="M0 28 l26 -14" stroke-width="3"/>
    <circle class="glyph-fill" cx="0" cy="28" r="4"/>
  </g>

  <g class="icon-budgeting" transform="translate(600 1005)">
    <circle class="icon-badge" r="54" fill="var(--orange)"/>
    <rect class="glyph-fill" x="-27" y="-34" width="54" height="70" rx="6"/>
    <rect x="-12" y="-40" width="24" height="12" rx="4" fill="var(--white)" stroke="var(--orange)" stroke-width="3"/>
    <path d="M-16 -4 l10 -8 l8 6 l14 -12" fill="none" stroke="var(--orange)" stroke-width="4" stroke-linecap="round" stroke-linejoin="round"/>
    <path d="M-16 10 h4 M-4 10 h20 M-16 22 h4 M-4 22 h20" stroke="var(--orange)" stroke-width="4" stroke-linecap="round"/>
  </g>

  <g class="icon-risk" transform="translate(324 893)">
    <circle class="icon-badge" r="54" fill="var(--sky)"/>
    <circle class="glyph" r="28" stroke-width="10" stroke-dasharray="8 6"/>
    <circle class="glyph" r="21" stroke-width="4"/>
    <path class="glyph-fill" d="M0 -14 l14 24 h-28 z"/>
    <path d="M0 -6 v8 M0 6 v1" stroke="var(--sky)" stroke-width="3" stroke-linecap="round"/>
  </g>

  <g class="icon-compliance" transform="translate(195 600)">
    <circle class="icon-badge" r="54" fill="var(--royal)"/>
    <path class="glyph" d="M-28 -26 v52 h46" stroke-width="3"/>
    <rect class="glyph" x="-22" y="-32" width="42" height="56" stroke-width="3"/>
    <path class="glyph" d="M-16 -22 h6 v6 h-6z M-4 -19 h16 M-16 -8 h6 v6 h-6z M-4 -5 h12 M-16 6 h6 v6 h-6z M-4 9 h8" stroke-width="3"/>
    <path d="M18 0 l14 5 v10 c0 9 -7 15 -14 18 c-7 -3 -14 -9 -14 -18 v-10z" fill="var(--white)" stroke="var(--royal)" stroke-width="3"/>
    <path d="M12 16 l5 4 l8 -9" fill="none" stroke="var(--royal)" stroke-width="3" stroke-linecap="round" stroke-linejoin="round"/>
  </g>

  <g class="icon-communication" transform="translate(305 322)">
    <circle class="icon-badge" r="54" fill="var(--navy)"/>
    <circle class="glyph-fill" cx="-24" cy="-32" r="5"/><path class="glyph-fill" d="M-34 -18 a10 9 0 0 1 20 0z"/>
    <circle class="glyph-fill" cx="24" cy="-32" r="5"/><path class="glyph-fill" d="M14 -18 a10 9 0 0 1 20 0z"/>
    <circle class="glyph-fill" cx="-24" cy="16" r="5"/><path class="glyph-fill" d="M-34 30 a10 9 0 0 1 20 0z"/>
    <circle class="glyph-fill" cx="24" cy="16" r="5"/><path class="glyph-fill" d="M14 30 a10 9 0 0 1 20 0z"/>
    <circle class="glyph" r="28" stroke-width="3" stroke-dasharray="14 14"/>
    <path class="glyph-fill" d="M-16 -10 h32 a4 4 0 0 1 4 4 v12 a4 4 0 0 1 -4 4 h-12 l-4 6 l-4 -6 h-12 a4 4 0 0 1 -4 -4 v-12 a4 4 0 0 1 4 -4z"/>
    <circle cx="-7" cy="0" r="2" fill="var(--navy)"/><circle cx="0" cy="0" r="2" fill="var(--navy)"/><circle cx="7" cy="0" r="2" fill="var(--navy)"/>
  </g>
</svg>
</body>
</html>
```